Teskar Business Cards

We need new Business Cards for our startup. It just launched.It is working in the high-end it-market. Specifically in the cloud area. We are a hybrid cloud company. The company logo is attached. We are a Swiss based company. Information visible on the card is: 1. Logo 2. Company Name: Teskar AG 3. Subtitle: Hybrid Clouds. 3. Name: Lukas Brenner 4. Adress: Holderweg 12a, 8462 Eglisau, Switzerland 5. Email: lukas@teskar.example. 6. Mobile: +41 79 304 62 18. It should be a grey/white design. Similar to the attached logo. It should have class, high-quality but not too much color and no gold used.

I forgot to add my Position. Please use Founder / CEO. thanks lukas

```html
<!DOCTYPE html>
<html lang="en">
<head>
<meta charset="utf-8">
<title>Teskar AG – Business Card</title>
<link href="https://fonts.googleapis.com/css2?family=Lato:wght@400;700&display=swap" rel="stylesheet">
<style>
  :root {
    --page-bg: #e4e4e4;
    --card-bg: #ffffff;
    --ink: #4f4f51;
    --ink-soft: #5e5e60;
    --rule: #5a5a5c;
    --band-dark: #231f20;
    --band-grey: #97979a;
    --band-edge: #ffffff;
  }
  * { margin: 0; padding: 0; box-sizing: border-box; }
  html, body {
    width: 1200px; height: 750px; overflow: hidden;
    background: var(--page-bg);
    font-family: "Lato", sans-serif;
    color: var(--ink);
  }
  .card {
    position: absolute; left: 120px; top: 100px;
    width: 960px; height: 551px;
    background: var(--card-bg);
    box-shadow: 0 4px 18px rgba(0,0,0,0.18);
    overflow: hidden;
  }
  .brand {
    position: absolute; top: 78px; left: 0; width: 100%;
    display: flex; justify-content: center; align-items: center; gap: 26px;
  }
  .brand-mark {
    width: 34px; height: 34px; border-radius: 50%;
    background: var(--band-grey);
  }
  .brand-name {
    font-weight: 400; font-size: 46px; letter-spacing: 14px;
    color: var(--ink-soft);
  }
  .identity {
    position: absolute; top: 248px; left: 83px; right: 85px;
    display: flex; justify-content: space-between;
  }
  .identity .title { font-weight: 700; font-size: 30px; line-height: 1.1; }
  .identity .sub { font-weight: 400; font-size: 22px; margin-top: 4px; color: var(--ink-soft); }
  .identity .company { text-align: right; }
  .rule {
    position: absolute; top: 330px; left: 83px; right: 85px;
    height: 3px; background: var(--rule);
  }
  .contacts {
    position: absolute; top: 383px; left: 83px;
    font-size: 22px; line-height: 29px;
  }
  .contacts li { list-style: none; display: flex; align-items: center; gap: 14px; }
  .contacts svg { width: 22px; height: 22px; fill: var(--band-dark); }
  .address {
    position: absolute; top: 379px; right: 85px;
    text-align: right; font-size: 22px; line-height: 29px;
    font-style: normal;
  }
  .footer-band { position: absolute; left: 0; bottom: 0; width: 960px; height: 72px; }
</style>
</head>
<body>
  <div class="card">
    <div class="brand">
      <span class="brand-mark"></span>
      <span class="brand-name">TESKAR</span>
    </div>

    <div class="identity">
      <div class="person">
        <div class="title">LUKAS BRENNER</div>
        <div class="sub">Founder / CEO</div>
      </div>
      <div class="company">
        <div class="title">TESKAR AG</div>
        <div class="sub">Hybrid Clouds</div>
      </div>
    </div>

    <div class="rule"></div>

    <ul class="contacts">
      <li>
        <svg viewBox="0 0 24 24" aria-hidden="true"><path d="M7 1h10a2 2 0 0 1 2 2v18a2 2 0 0 1-2 2H7a2 2 0 0 1-2-2V3a2 2 0 0 1 2-2zm0 3v14h10V4H7zm5 15.2a1.2 1.2 0 1 0 0 2.4 1.2 1.2 0 0 0 0-2.4z"/></svg>
        +41 79 304 62 18
      </li>
      <li>
        <svg viewBox="0 0 24 24" aria-hidden="true"><path d="M2 5h20v14H2V5zm2 2v.4l8 5.3 8-5.3V7H4zm16 2.8-8 5.3-8-5.3V17h16V9.8z"/></svg>
        lukas@teskar.example
      </li>
    </ul>

    <address class="address">
      Holderweg 12a<br>
      8462 Eglisau, Switzerland
    </address>

    <svg class="footer-band" viewBox="0 0 960 72" aria-hidden="true">
      <rect x="0" y="0" width="960" height="72" fill="var(--band-dark)"/>
      <polygon points="96,0 876,0 848,32 124,32" fill="var(--band-grey)" stroke="var(--band-edge)" stroke-width="4"/>
    </svg>
  </div>
</body>
</html>
```